Poster announcing University Web Analytics talk

We need a poster to announce an upcoming talk on Web Analytics at the local University. The event is addressed to final year students (mostly in Informatic Engineering, although other majors are wellcomed as well) who may be interested in specializing in this rising field.

The poster should present a brief list of the points we'll be addressing, as well as the place and time of the meeting. Also, it must feature our company logo (check the uploads section to find it) and our website url: http://www.brasslanternworks.net.

Texts for the poster:

Headline: "Get specialized in Web & Mobile Analytics"

Topics that will be covered:
- Introduction to Analytics, market, work opportunities
- Know the basics of an Analytics project: planning, phases, implementation
- Job bank: bring your CV!

Event information: "Thursday 20th June at the Escuela de Sistemas, Instituto Pelayo Norte". [A space to fill with the time must be provided here]

However, we'll be translating all the text to Spanish later, so we'll need a file where we can modify the text layers.
Updates

Thanks to all of you, we're receiving so many excellent works!

We had missed to include some important information on the brief - we didn't say anything about the colors, and we have been getting some designs based in dark colors. Now, it doesn't matter what colors you use, but we'd like better a brighter design (no matter if the color combination is more playful or either rather serious). This is going to be a free talk addressed to last year students, so we want to transmit a feeling of an interesting, easy and entertaining afternoon.

I hope these comments are helpful, please reach me with any question or comment. 

Thanks a lot again!
Nuria 
BL team

Target Market(s)

Final year students and graduates.

Industry/Entity Type

Bank

Requirements
Must have
• Design must be submitted in vector format, preferably .psd. We must be able to modify the text layers. Our logo (check the files section) and website url (http://www.brasslanternworks.net) must be included
Nice to have
• Illustrations making reference to Analytics (charts, statistics, code) and/or the internet will be a plus!

```html
<!DOCTYPE html>
<html lang="en">
<head>
<meta charset="utf-8">
<title>Get Specialized in Web &amp; Mobile Analytics</title>
<link rel="stylesheet" href="https://fonts.googleapis.com/css2?family=Anton&family=Arimo:wght@400;700&display=swap">
<style>
  :root {
    --band-grey: #e4e4e6;
    --rule-grey: #c9c9cc;
    --headline-blue: #2a3896;
    --body-ink: #1a1a1a;
    --brand-navy: #1f4a6b;
    --stage-white: #ffffff;
  }
  html, body {
    margin: 0;
    padding: 0;
    overflow: hidden;
    background: #ffffff;
  }
  .poster {
    position: relative;
    width: 902px;
    height: 1200px;
    overflow: hidden;
    background: var(--stage-white);
    font-family: "Arimo", Arial, sans-serif;
    color: var(--body-ink);
  }
  .headline-band {
    position: absolute;
    left: 0; top: 0;
    width: 902px; height: 336px;
    background: var(--band-grey);
    border-bottom: 6px solid var(--rule-grey);
    box-sizing: border-box;
  }
  .headline {
    position: absolute;
    left: 0; right: 0; top: 78px;
    margin: 0;
    text-align: center;
    white-space: nowrap;
    font-family: "Anton", "Arial Narrow", sans-serif;
    font-weight: 400;
    font-size: 78px;
    line-height: 97px;
    letter-spacing: 0.5px;
    text-transform: uppercase;
    color: var(--headline-blue);
  }
  .hero-illustration {
    position: absolute;
    left: 0; top: 342px;
    width: 902px; height: 456px;
    background:
      radial-gradient(ellipse 22% 40% at 50% 48%, #5b6470 0%, #3f9fd8 45%, rgba(63,159,216,0) 70%),
      radial-gradient(ellipse 30% 22% at 22% 70%, #38b6b3 0%, rgba(56,182,179,0) 70%),
      radial-gradient(ellipse 26% 22% at 78% 70%, #d8a24a 0%, rgba(216,162,74,0) 70%),
      radial-gradient(ellipse 24% 18% at 32% 22%, #d9413c 0%, rgba(217,65,60,0) 70%),
      radial-gradient(ellipse 20% 20% at 82% 42%, #55b84a 0%, rgba(85,184,74,0) 70%),
      var(--stage-white);
  }
  .info-band {
    position: absolute;
    left: 0; top: 798px;
    width: 902px; height: 402px;
    background: var(--band-grey);
    border-top: 6px solid var(--rule-grey);
    box-sizing: border-box;
  }
  .topics {
    position: absolute;
    left: 40px; top: 30px;
    width: 520px;
    margin: 0; padding: 0;
    list-style: none;
  }
  .topics li {
    position: relative;
    padding-left: 30px;
    font-size: 21px;
    line-height: 29px;
    margin-bottom: 33px;
  }
  .topics li::before {
    content: "";
    position: absolute;
    left: 0; top: 10px;
    width: 10px; height: 10px;
    border-radius: 50%;
    background: var(--body-ink);
  }
  .event-time {
    font-weight: 700;
  }
  .brand {
    position: absolute;
    left: 652px; top: 278px;
    display: flex;
    align-items: center;
    gap: 10px;
  }
  .brand-square {
    width: 34px; height: 34px;
    background: var(--brand-navy);
  }
  .brand-name {
    font-weight: 700;
    font-size: 22px;
    line-height: 24px;
    color: var(--brand-navy);
    width: 150px;
  }
  .brand-url {
    position: absolute;
    right: 30px; top: 350px;
    font-size: 15px;
    line-height: 18px;
    color: var(--brand-navy);
  }
</style>
</head>
<body>
  <main class="poster">
    <header class="headline-band">
      <h1 class="headline">Get specialized in<br>Web &amp; Mobile Analytics</h1>
    </header>

    <div class="hero-illustration" role="img" aria-label="Illustration of a smartphone surrounded by colourful 3D bar and pie charts, stacks of gold coins and curved red and green arrows"></div>

    <section class="info-band">
      <ul class="topics">
        <li>Introduction to Analytics, market, work oppor-<br>tunities</li>
        <li>Know the basics of an Analytics project: plan-<br>ning, phases, implementation</li>
        <li>Job bank: bring your CV!</li>
        <li>"Thursday 20th June at the Escuela de Sistemas, Instituto Pelayo Norte". <span class="event-time">17:00 h</span></li>
      </ul>
      <div class="brand">
        <span class="brand-square"></span>
        <span class="brand-name">Brass Lantern Works</span>
      </div>
      <p class="brand-url" style="margin:0">http://www.brasslanternworks.net</p>
    </section>
  </main>
</body>
</html>
```